Norvale Labs" Voyage Check Kit" Instructions Cards

We need to design two 4.25" x 5.5" 2-sided COVID-19 Specimen Collection Instructions Cards. One card is for the collection and testing of RT-PCR Nasal Swab Specimen and the second card is for the collection and testing of a Rapid Antigen Nasal Swab specimen.

Each card will be 4.25" x 5.5", 2-sided, laminated no-edge seal, with 3 color front and 2 color back.

RT-PCR Nasal Swab Collection Kit Instructions:
1. Please see an "example only" of a collection test kit instructions done for PCR Saliva test (see attached 2-sided card).
2. Please see attached PDF of the RT-PCR Nasal Swab Collection instructions. We will need to follow these collection steps instructions but design our own illustrations. With this set of instructions we will have a total of 8 steps.
3. Please see our Nasal Swab Collection device (see attached images), as our nasal swab is a dry collection device.

Rapid Antigen Nasal Swab Collection Kit Instructions:
1. Please see an "example" of a collection test kit instructions done for Rapid Antigen Test (see attached image with instructions). we will need to follow these steps 7 steps and will revise/shorten the copy.
2. We will have a total of 8 steps and will provide detailed copy for each step.

Please email me with any questions you may have: tmalloway@norvalediagnostics.example

Thank you

Tad

```html
<!DOCTYPE html>
<html lang="en">
<head>
<meta charset="utf-8">
<title>Norvale Labs Voyage Check Kit – Instruction Cards</title>
<link href="https://fonts.googleapis.com/css2?family=Poppins:wght@300;400;600&display=swap" rel="stylesheet">
<style>
  :root {
    --backdrop: #a9a9a9;
    --card: #ffffff;
    --header-bar: #666666;
    --header-text: #ffffff;
    --body-text: #1e1e1e;
    --step-number: #a5a5a5;
    --art-skin: #f6c3a3;
    --art-grey: #d9d9d9;
    --art-red: #9b1b1b;
    --brand: #2d2d2d;
    --brand-dot: #3b5fb0;
  }
  * { box-sizing: border-box; margin: 0; padding: 0; }
  html, body { width: 1200px; height: 794px; overflow: hidden; }
  body {
    position: relative;
    background: var(--backdrop);
    font-family: "Poppins", sans-serif;
    color: var(--body-text);
  }
  .card {
    position: absolute;
    top: 87px;
    width: 483px;
    height: 623px;
    background: var(--card);
  }
  .card--pcr { left: 88px; }
  .card--antigen { left: 637px; }
  .card__title {
    position: absolute;
    left: 26px;
    top: 21px;
    width: 437px;
    height: 28px;
    background: var(--header-bar);
    color: var(--header-text);
    font-weight: 600;
    font-size: 12.6px;
    line-height: 28px;
    padding-left: 10px;
    letter-spacing: 0.1px;
  }
  .card--antigen .card__title { padding-left: 16px; }
  .step { position: absolute; left: 0; }
  .step__num {
    position: absolute;
    left: 29px;
    top: -3px;
    font-weight: 300;
    font-size: 26px;
    line-height: 1;
    color: var(--step-number);
  }
  .card--antigen .step__num { left: 28px; }
  .step__text {
    position: absolute;
    left: 54px;
    font-size: 10.6px;
    line-height: 12.4px;
    font-weight: 400;
  }
  .art {
    position: absolute;
    border-radius: 6px;
  }
  .art--skin { background: linear-gradient(135deg, var(--art-skin), #fbe2d2); }
  .art--kit { background: linear-gradient(135deg, var(--art-grey), #f1f1f1); }
  .art--tube { background: linear-gradient(160deg, #f3f3f3, var(--art-grey) 70%, #e7c9c9); }
  .brand {
    position: absolute;
    left: 155px;
    top: 577px;
    display: flex;
    align-items: center;
    gap: 8px;
    font-weight: 600;
    font-size: 24px;
    color: var(--brand);
  }
  .brand__dot {
    width: 16px; height: 16px; border-radius: 50%;
    background: var(--brand-dot);
  }
</style>
</head>
<body>

<section class="card card--pcr">
  <h2 class="card__title">RT-PCR NASAL SWAB COLLECTION KIT INSTRUCTIONS:</h2>

  <div class="step" style="top:90px">
    <span class="step__num">1</span>
    <p class="step__text" style="width:280px">Remove contents where you will open the collection kit. Remove and layout contents of kit. Read instructions before starting specimen collection.</p>
  </div>
  <div class="art art--kit" role="img" aria-label="Collection kit contents: biohazard bag, swab and tube" style="left:364px;top:71px;width:78px;height:77px"></div>

  <div class="step" style="top:184px">
    <span class="step__num">2</span>
    <p class="step__text" style="width:285px">Remove the swab from the package. Do not touch the soft end with your hands a anything else.</p>
  </div>
  <div class="art art--skin" role="img" aria-label="Hands peeling open the swab package" style="left:360px;top:168px;width:78px;height:71px"></div>

  <div class="step" style="top:259px">
    <span class="step__num">3</span>
    <p class="step__text" style="width:370px">Insert &amp; slowly rotate the swab, gently pressing against the inside of each nostril at least 4 times for a total of 15 seconds. Get as much nasal discharge as possible on the soft end of the swab.</p>
  </div>

  <div class="step" style="top:345px">
    <span class="step__num">4</span>
    <p class="step__text" style="width:150px">Gently Remove the swab</p>
  </div>
  <div class="art art--skin" role="img" aria-label="Swab being rotated inside the nostril" style="left:223px;top:328px;width:101px;height:39px"></div>
  <div class="art art--skin" role="img" aria-label="Swab being withdrawn from the nostril" style="left:342px;top:328px;width:101px;height:39px"></div>

  <div class="step" style="top:415px">
    <span class="step__num">5</span>
    <p class="step__text" style="width:270px">Place the swab In the sterile tube and snap off the end of the swab at the break line, so that It fits comfortably In the tube. Place the cap on the tube and screw down tightly to prevent leakage.</p>
  </div>
  <div class="art art--skin" role="img" aria-label="Hands placing the swab into the sterile tube" style="left:357px;top:406px;width:94px;height:84px"></div>

  <div class="step" style="top:513px">
    <span class="step__num">6</span>
    <p class="step__text" style="width:260px">Place the tube containing the swab In the biohazard bag provided and seal the bag. and follow the instructions on the card for shipping to lab for testing.</p>
  </div>
  <div class="art art--tube" role="img" aria-label="Sealed biohazard bag holding the specimen tube" style="left:350px;top:502px;width:91px;height:76px"></div>

  <div class="brand"><span class="brand__dot"></span><span>NORVALE LABS</span></div>
</section>

<section class="card card--antigen">
  <h2 class="card__title">RAPID ANTIGEN NASAL SWAB COLLECTION KIT INSTRUCTIONS</h2>

  <div class="step" style="top:88px">
    <span class="step__num">1</span>
    <p class="step__text" style="width:280px">Remove the Swab &amp; Test Device from their packaging. Place the Test Device on a horizontal (flat) surface forrunning the test.</p>
  </div>
  <div class="art art--skin" role="img" aria-label="Hands removing the test device from its pouch" style="left:344px;top:66px;width:108px;height:70px"></div>

  <div class="step" style="top:147px">
    <span class="step__num">2</span>
    <p class="step__text" style="width:275px">Insert the entire collection tip of the swab provided (usually 1/2 to 3/4 of an inch, or 1 to 1.5 cm) inside the nostril. Firmly sample the nasal wall by rotating the swab in a circular path against the nasal wall at least 4 times. Take approximately 15 seconds to collect the specimen. Be sure to collect any nasal drainage that may be present on the swab. &nbsp;Repeat in the other nostril using the same swab.</p>
  </div>
  <div class="art art--skin" role="img" aria-label="Profile with swab inserted in the nostril" style="left:347px;top:148px;width:99px;height:71px"></div>

  <div class="step" style="top:269px">
    <span class="step__num">3</span>
    <p class="step__text" style="width:275px">The Buffer Solution Vial cap is composed of two parts (purple and white). Remove the entire cap. Stir the swab into the Buffer Solution, ensuring that the swab head is fully submerged by tilting the vial. Twist the swab back and forth 20 times in the Buffer Solution. Poll the swab head against the inner wall of the vial to release the liquid from the swab, then discard the swab.</p>
  </div>
  <div class="art art--kit" role="img" aria-label="Buffer vial with cap removed and swab stirred" style="left:340px;top:265px;width:103px;height:81px"></div>

  <div class="step" style="top:393px">
    <span class="step__num">4</span>
    <p class="step__text" style="width:230px">Close the entire cap tightly.Immediately perform steps 5-7.</p>
  </div>
  <div class="art art--kit" role="img" aria-label="Buffer vial with cap closed and dropper tip exposed" style="left:319px;top:366px;width:122px;height:99px"></div>

  <div class="step" style="top:448px">
    <span class="step__num">5</span>
    <p class="step__text" style="width:260px">Remove the purple top half of the cap to expose the dropper tip.</p>
  </div>

  <div class="step" style="top:511px">
    <span class="step__num">6</span>
    <p class="step__text" style="width:275px">Hold the vial vertically above the sample well (S). Slowly squeeze and apply 3 drops of the Buffer Solution into the sample well (S) of the Test Device.</p>
  </div>
  <div class="art art--skin" role="img" aria-label="Hand squeezing drops onto the test device" style="left:335px;top:475px;width:83px;height:68px"></div>

  <div class="step" style="top:569px">
    <span class="step__num">7</span>
    <p class="step__text" style="width:305px">Read the test line (T) and control line (C) results promptly at 20 minutes, and not earlierto ensure proper test performance. Results after 25 minutes should not be used.</p>
  </div>
  <div class="art art--kit" role="img" aria-label="Stopwatch showing the waiting time" style="left:381px;top:548px;width:53px;height:59px;border-radius:50%"></div>
</section>

</body>
</html>
```